HiItsJonBrell.com needs a modern, eye-catching business card design

My name is Jon Brell and I own a video training (software development industry) website. I need a business card design that is eye catching for when I travel to conferences or do seminars. I would prefer something simple but bold. Something along the lines of this: https://pixvaultstatic.example/gallery_img/530172/44018/44018_9917302_530172_image.jpg

Note that I do not have a specific logo, but I do have an caricature I use on my site of myself. I've not attached it because I'm not really a fan of having it on my business cards. I would prefer lettering instead of an image. You can go to my website (https://hiitsjonbrell.com) for inspiration.

I want to add the following information on my card (the order of these, their size, and their casing is up to you):

Jon Brell
jon@HiItsJonBrell.com
@HiItsJonBrell
HiItsJonBrell.com
vidsharehub.example/HiItsJonBrell

I would also like to have somewhere on the card a small ad that says "Get a free course at https://HiItsJonBrell.com/FreeCourse". Feel free to play with that wording or layout if you need. I would prefer this text to be at the bottom of the card and subtle. Some small eye-catching thing might be ok but nothing huge or garish.

I plan on printing this card at pressquill.example (https://www.pressquill.example/us/design-guidelines/business-cards.html). I would like it to be the standard size (3.66" x 2.16"). I would prefer rounded corners and horizontal orientation. This is a two-side design. I would prefer the side with all of the information be primarily white but I like color text (again, flexible on that). On the front side, I like simple. Maybe just HiItsJonBrell.com (casing on that is up to you - whatever looks and reads the best - that goes for all of the casing). As for font choices, I prefer a modern, clean font. For example, Open Sans Light can be a nice option.

Website Info (might be helpful for the card):
Color Palette

Darkest blue - #263246
Alternate blue - #2F4E6A
Light blue - #2A98C3
Orange - #FF6201
White - #FFFFFF

Font for Jon Brell Logo

Jellyka Estryas Handwriting
http://www.typecrate.example/jellyka_estryas_handwriting.font

Fonts for Site Content and VidShare Thumbnails

Lovelo (bold title font)
http://www.glyphmill.example/lovelo-font/

Open Sans (body font)
http://www.letterbarn.example/fonts/open-sans

Industry/Entity Type

Software Development

Contact Information for Business Card

Jon Brell
jon@HiItsJonBrell.com
@HiItsJonBrell
HiItsJonBrell.com
vidsharehub.example/HiItsJonBrell

Get a free course at https://HiItsJonBrell.com/FreeCourse

Colors

Designer to choose colors to be used in the design.

Requirements
Nice to have
• Modern color - maybe primarily a color on the front and then that color as an accent on the back.
Should not have
• Lots of colors - I LOVE color but do not want a rainbow of colors on the card.

```html
<!DOCTYPE html>
<html lang="en">
<head>
<meta charset="utf-8">
<title>Jon Brell – Business Card</title>
<link rel="stylesheet" href="https://fonts.googleapis.com/css2?family=Open+Sans:wght@300;400;600;700&display=swap">
<style>
  :root {
    --navy: #263246;
    --orange: #FF6201;
    --white: #FFFFFF;
    --paper: #EEEEEE;
    --ink: #1F2530;
  }
  html, body {
    margin: 0;
    padding: 0;
    overflow: hidden;
    background: var(--paper);
  }
  .card {
    position: relative;
    width: 1200px;
    height: 355px;
    overflow: hidden;
    font-family: "Open Sans", Arial, sans-serif;
    background: var(--paper);
  }
  .card-shapes {
    position: absolute;
    inset: 0;
  }
  .front-name {
    position: absolute;
    left: 114px;
    top: 118px;
    width: 341px;
    height: 103px;
    border-top: 3px solid var(--orange);
    border-bottom: 3px solid var(--orange);
    box-sizing: border-box;
    display: flex;
    align-items: center;
    justify-content: center;
    color: var(--white);
    font-weight: 400;
    font-size: 56px;
    letter-spacing: 1px;
    margin: 0;
  }
  .back-name {
    position: absolute;
    left: 770px;
    top: 68px;
    width: 278px;
    margin: 0;
    padding-bottom: 8px;
    border-bottom: 3px solid var(--orange);
    text-align: center;
    color: var(--ink);
    font-weight: 700;
    font-size: 21px;
  }
  .contact-list {
    position: absolute;
    left: 778px;
    top: 118px;
    margin: 0;
    padding: 0;
    list-style: none;
  }
  .contact-item {
    display: flex;
    align-items: center;
    height: 35px;
    color: var(--ink);
    font-size: 19px;
  }
  .contact-icon {
    width: 22px;
    height: 22px;
    margin-right: 10px;
    flex: none;
  }
  .contact-mark {
    width: 16px;
    height: 16px;
    margin: 0 13px 0 3px;
    background: var(--ink);
    flex: none;
  }
  .contact-mark.round { border-radius: 50%; }
  .free-course {
    position: absolute;
    right: 28px;
    top: 308px;
    margin: 0;
    color: var(--ink);
    font-size: 16px;
    font-weight: 600;
  }
</style>
</head>
<body>
<main class="card">
  <svg class="card-shapes" width="1200" height="355" viewBox="0 0 1200 355" aria-hidden="true">
    <path fill="#FFFFFF" d="M700 0 H1170 A30 30 0 0 1 1200 30 V325 A30 30 0 0 1 1170 355 H600 V100 A100 100 0 0 1 700 0 Z"/>
    <path fill="#263246" d="M20 0 H600 V255 A100 100 0 0 0 700 355 H20 A20 20 0 0 1 0 335 V20 A20 20 0 0 1 20 0 Z"/>
  </svg>

  <h1 class="front-name">JON BRELL</h1>

  <h2 class="back-name">JON BRELL</h2>
  <ul class="contact-list">
    <li class="contact-item">
      <svg class="contact-icon" viewBox="0 0 22 22" aria-hidden="true">
        <rect x="2" y="5" width="18" height="13" fill="none" stroke="#1F2530" stroke-width="2"/>
        <path d="M2 5 L11 13 L20 5" fill="none" stroke="#1F2530" stroke-width="2"/>
      </svg>
      jon@HiItsJonBrell.com
    </li>
    <li class="contact-item"><span class="contact-mark round"></span>@HiItsJonBrell</li>
    <li class="contact-item"><span class="contact-mark"></span>vidsharehub.example/HiItsJonBrell</li>
    <li class="contact-item">
      <svg class="contact-icon" viewBox="0 0 22 22" aria-hidden="true">
        <g fill="none" stroke="#1F2530" stroke-width="1.6">
          <circle cx="11" cy="11" r="8.5"/>
          <ellipse cx="11" cy="11" rx="3.8" ry="8.5"/>
          <path d="M2.5 11 H19.5 M4 6.5 H18 M4 15.5 H18"/>
        </g>
      </svg>
      HiItsJonBrell.com
    </li>
  </ul>

  <p class="free-course">Free course in: https://HiItsJonBrell.com/FreeCourse</p>
</main>
</body>
</html>
```